MD Trailcraft & Wildland Fair

I need a 1 page flyer for promotion of an upcoming sportsman and outdoor show(expo). would like the flyer to be able to be printed in B&W and color! show will include all things to do with the out doors, hunting fishing boating hiking atv camping rvs motorcycles. the event will have a kids zone, events games and activities for kids. there will be vendors showing the newest products. guest speakers and industry experts giving training and advice. this show will have something for everyone. food trucks and concessions. 200+ vendors. waterfould calling competition. deer/buck scoring casting competition for kids 3D Archery competitions

Target Market(s)

anyone event open to all ages!

Colors
ec1f27
000000
fbed22

Requirements
Must have
• date- september 1-2 2018
• location Pelling valley expo 4837 orchardmill rd east calverton MD 21652
• facebook - mdtrailcraftfair
• email mdtrailcraftfair@quorvex.com
• web www.mdtrailcraftfair.com
• vendor spaces still available! sign up now space going fast
Nice to have
• would like some thing that can be both printed in B&W and Color, and still have a great affect.
Should not have
• open to any suggestions

```html
<!DOCTYPE html>
<html lang="en">
<head>
<meta charset="utf-8">
<title>MD Trailcraft &amp; Wildland Fair – Flyer</title>
<link href="https://fonts.googleapis.com/css2?family=Bebas+Neue&family=Open+Sans:wght@600;700&family=Caveat+Brush&display=swap" rel="stylesheet">
<style>
  :root {
    --page: #ffffff;
    --white: #ffffff;
    --rule: rgba(255,255,255,0.85);
  }
  html, body { margin: 0; padding: 0; overflow: hidden; }
  body { width: 1200px; height: 1000px; background: var(--page); position: relative; }
  h1, h2, h3, p, ul { margin: 0; }

  .flyer {
    position: absolute; top: 126px; width: 536px; height: 756px; overflow: hidden;
    font-family: "Open Sans", Arial, sans-serif; color: var(--white);
  }
  .flyer--mono {
    left: 50px;
    --bg-top: #3e3e3e; --bg-mid: #6a6a6a; --bg-low: #4a4a4a;
    --accent: #c4c4c4; --banner: #c4c4c4; --banner-text: #3a3a3a;
    --stripe: #9a9a9a; --band: #565656; --pin: #8a8a8a;
    --photo-a: #d9d9d9; --photo-b: #7d7d7d; --contact: #e2e2e2;
  }
  .flyer--color {
    left: 617px;
    --bg-top: #1f2a6b; --bg-mid: #3a3f7e; --bg-low: #283473;
    --accent: #f0c21e; --banner: #eec124; --banner-text: #1e2656;
    --stripe: #1aa3e0; --band: #2b4fa8; --pin: #1aa3e0;
    --photo-a: #9ec3d6; --photo-b: #c7a25c; --contact: #f0c21e;
  }

  .backdrop {
    position: absolute; inset: 0;
    background:
      linear-gradient(160deg, transparent 55%, rgba(255,255,255,0.08) 56%, transparent 75%),
      linear-gradient(180deg, var(--bg-top) 0%, var(--bg-mid) 45%, var(--bg-low) 100%);
  }

  .title { position: absolute; left: 0; top: 0; font-family: "Bebas Neue", Impact, sans-serif; font-weight: 400; line-height: 1; }
  .title span { position: absolute; white-space: nowrap; }
  .title__top { left: 47px; top: 26px; font-size: 42px; color: var(--white); }
  .title__and { left: 24px; top: 52px; font-family: "Caveat Brush", cursive; font-size: 34px; color: var(--white); }
  .title__main { left: 20px; top: 86px; font-size: 80px; color: var(--accent); }
  .title__end { left: 63px; top: 154px; font-size: 80px; color: var(--white); }

  .date-banner {
    position: absolute; left: 292px; top: 26px; width: 244px; height: 54px;
    background: var(--banner); clip-path: polygon(0 0, 100% 0, 100% 100%, 14% 100%);
    font-family: "Bebas Neue", Impact, sans-serif; font-size: 31px; color: var(--banner-text);
    display: flex; align-items: center; justify-content: flex-end; padding-right: 16px; box-sizing: border-box;
  }
  .date-stripe {
    position: absolute; left: 388px; top: 80px; width: 148px; height: 14px;
    background: var(--stripe); clip-path: polygon(0 0, 100% 0, 100% 100%, 12% 100%);
  }

  .tagline {
    position: absolute; left: 266px; top: 124px; width: 260px; text-align: center;
    font-family: "Caveat Brush", cursive; font-size: 36px; line-height: 30px; color: var(--white);
  }

  .photo {
    position: absolute; width: 180px; height: 126px; background: var(--white);
    border-radius: 14px; padding: 9px; box-shadow: 0 3px 8px rgba(0,0,0,0.35);
  }
  .photo__fill { width: 100%; height: 100%; border-radius: 6px; background: linear-gradient(135deg, var(--photo-a), var(--photo-b)); }
  .photo--fishing { left: 33px; top: 228px; transform: rotate(4deg); }
  .photo--boat { left: 298px; top: 380px; transform: rotate(4deg); }
  .photo--hiking { left: 33px; top: 512px; transform: rotate(4deg); }

  .section-heading {
    position: absolute; font-family: "Bebas Neue", Impact, sans-serif; font-weight: 400; font-size: 33px;
    line-height: 1; color: var(--accent); white-space: nowrap;
  }
  .section-heading--fishing { left: 265px; top: 232px; }
  .section-heading--boat { left: 134px; top: 382px; }
  .section-heading--hiking { left: 258px; top: 531px; }

  .rule { position: absolute; height: 0; border-top: 2px dotted var(--rule); }

  .highlights { position: absolute; left: 265px; top: 286px; padding: 0; list-style: none; font-size: 12.5px; line-height: 16px; font-weight: 600; }
  .highlights li { position: relative; padding-left: 14px; }
  .highlights svg { position: absolute; left: 0; top: 3px; }
  .tick { stroke: var(--accent); }

  .vendor-note { position: absolute; left: 24px; top: 434px; width: 246px; text-align: center; font-size: 15.5px; line-height: 20px; font-weight: 700; }
  .vendor-note__hl { color: var(--accent); }

  .contact { position: absolute; left: 278px; top: 583px; }
  .contact__title { font-family: "Bebas Neue", Impact, sans-serif; font-weight: 400; font-size: 15px; line-height: 1; margin: 0 0 8px; letter-spacing: 0.2px; }
  .contact__list { list-style: none; padding: 0 0 0 14px; font-size: 12.5px; line-height: 18px; font-weight: 600; color: var(--contact); }
  .contact__list li { display: flex; align-items: center; gap: 7px; }
  .contact__icon { width: 10px; height: 10px; flex: none; }
  .contact__dot { width: 8px; height: 8px; background: var(--white); flex: none; margin: 0 1px; }

  .footer-band { position: absolute; left: 0; bottom: 0; width: 100%; height: 74px; background: var(--band); }
  .venue { position: absolute; left: 105px; top: 700px; display: flex; align-items: center; gap: 10px; }
  .venue__pin { width: 29px; height: 29px; border-radius: 50%; background: var(--pin); display: flex; align-items: center; justify-content: center; }
  .venue__text { font-size: 15.5px; line-height: 19px; font-weight: 700; }
</style>
</head>
<body>

<section class="flyer flyer--mono">
  <div class="backdrop" role="img" aria-label="Mountain landscape photograph with a hiker, in greyscale"></div>

  <h1 class="title">
    <span class="title__top">MD TRAILCRAFT</span>
    <span class="title__and">and</span>
    <span class="title__main">WILDLAND</span>
    <span class="title__end">FAIR</span>
  </h1>

  <div class="date-banner">SEPTEMBER 1-2 2018</div>
  <div class="date-stripe"></div>

  <p class="tagline">Come with us<br>to be Adventurist</p>

  <div class="photo photo--fishing"><div class="photo__fill" role="img" aria-label="Family fishing together by a river"></div></div>
  <h2 class="section-heading section-heading--fishing">FISHING EVENT</h2>
  <div class="rule" style="left:265px; top:274px; width:248px"></div>
  <ul class="highlights">
    <li><svg width="10" height="10" viewBox="0 0 10 10"><path class="tick" d="M1 5 L4 8 L9 1" fill="none" stroke-width="2"/></svg>200+ vendors</li>
    <li><svg width="10" height="10" viewBox="0 0 10 10"><path class="tick" d="M1 5 L4 8 L9 1" fill="none" stroke-width="2"/></svg>Waterfould calling competition</li>
    <li><svg width="10" height="10" viewBox="0 0 10 10"><path class="tick" d="M1 5 L4 8 L9 1" fill="none" stroke-width="2"/></svg>Deer/buck scoring casting competition<br>for kids</li>
  </ul>
  <div class="rule" style="left:265px; top:358px; width:248px"></div>

  <h2 class="section-heading section-heading--boat">BOAT EVENT</h2>
  <div class="rule" style="left:24px; top:421px; width:276px"></div>
  <p class="vendor-note">Vendor spaces still <span class="vendor-note__hl">available!</span><br>Sign up now. Space going fast</p>
  <div class="rule" style="left:24px; top:485px; width:276px"></div>
  <div class="photo photo--boat"><div class="photo__fill" role="img" aria-label="Group rafting in an inflatable boat"></div></div>

  <div class="photo photo--hiking"><div class="photo__fill" role="img" aria-label="Two hikers with backpacks on a trail"></div></div>
  <h2 class="section-heading section-heading--hiking">HIKING EVENT AND MORE</h2>
  <div class="rule" style="left:258px; top:568px; width:255px"></div>

  <div class="contact">
    <h3 class="contact__title">FOR MORE INFORMATIONS</h3>
    <ul class="contact__list">
      <li><span class="contact__dot"></span>mdtrailcraftfair</li>
      <li><svg class="contact__icon" viewBox="0 0 10 10"><rect x="0.5" y="1.5" width="9" height="7" fill="#fff"/><path d="M0.5 1.5 L5 5.5 L9.5 1.5" fill="none" stroke="#555" stroke-width="1"/></svg>mdtrailcraftfair@quorvex.com</li>
      <li><svg class="contact__icon" viewBox="0 0 10 10"><circle cx="5" cy="5" r="4.2" fill="none" stroke="#fff" stroke-width="1.2"/><path d="M0.8 5 H9.2 M5 0.8 C2.5 3.5 2.5 6.5 5 9.2 M5 0.8 C7.5 3.5 7.5 6.5 5 9.2" fill="none" stroke="#fff" stroke-width="1"/></svg>www.mdtrailcraftfair.com</li>
    </ul>
  </div>
  <div class="rule" style="left:195px; top:670px; width:341px"></div>

  <div class="footer-band"></div>
  <div class="venue">
    <span class="venue__pin"><svg width="12" height="16" viewBox="0 0 12 16"><path d="M6 0 C2.7 0 0 2.6 0 5.9 C0 10 6 16 6 16 C6 16 12 10 12 5.9 C12 2.6 9.3 0 6 0 Z" fill="#fff"/><circle cx="6" cy="6" r="2.2" fill="var(--pin)"/></svg></span>
    <span class="venue__text">Pelling Valley Expo, 4837 Orchardmill Rd<br>East Calverton, MD. 21652</span>
  </div>
</section>

<section class="flyer flyer--color">
  <div class="backdrop" role="img" aria-label="Mountain landscape photograph with a hiker, tinted blue"></div>

  <h1 class="title">
    <span class="title__top">MD TRAILCRAFT</span>
    <span class="title__and">and</span>
    <span class="title__main">WILDLAND</span>
    <span class="title__end">FAIR</span>
  </h1>

  <div class="date-banner">SEPTEMBER 1-2 2018</div>
  <div class="date-stripe"></div>

  <p class="tagline">Come with us<br>to be Adventurist</p>

  <div class="photo photo--fishing"><div class="photo__fill" role="img" aria-label="Family fishing together by a river"></div></div>
  <h2 class="section-heading section-heading--fishing">FISHING EVENT</h2>
  <div class="rule" style="left:265px; top:274px; width:248px"></div>
  <ul class="highlights">
    <li><svg width="10" height="10" viewBox="0 0 10 10"><path class="tick" d="M1 5 L4 8 L9 1" fill="none" stroke-width="2"/></svg>200+ vendors</li>
    <li><svg width="10" height="10" viewBox="0 0 10 10"><path class="tick" d="M1 5 L4 8 L9 1" fill="none" stroke-width="2"/></svg>Waterfould calling competition</li>
    <li><svg width="10" height="10" viewBox="0 0 10 10"><path class="tick" d="M1 5 L4 8 L9 1" fill="none" stroke-width="2"/></svg>Deer/buck scoring casting competition<br>for kids</li>
  </ul>
  <div class="rule" style="left:265px; top:358px; width:248px"></div>

  <h2 class="section-heading section-heading--boat">BOAT EVENT</h2>
  <div class="rule" style="left:24px; top:421px; width:276px"></div>
  <p class="vendor-note">Vendor spaces still <span class="vendor-note__hl">available!</span><br>Sign up now. Space going fast</p>
  <div class="rule" style="left:24px; top:485px; width:276px"></div>
  <div class="photo photo--boat"><div class="photo__fill" role="img" aria-label="Group rafting in a yellow inflatable boat"></div></div>

  <div class="photo photo--hiking"><div class="photo__fill" role="img" aria-label="Two hikers with backpacks on a trail"></div></div>
  <h2 class="section-heading section-heading--hiking">HIKING EVENT AND MORE</h2>
  <div class="rule" style="left:258px; top:568px; width:255px"></div>

  <div class="contact">
    <h3 class="contact__title">FOR MORE INFORMATIONS</h3>
    <ul class="contact__list">
      <li><span class="contact__dot"></span>mdtrailcraftfair</li>
      <li><svg class="contact__icon" viewBox="0 0 10 10"><rect x="0.5" y="1.5" width="9" height="7" fill="#fff"/><path d="M0.5 1.5 L5 5.5 L9.5 1.5" fill="none" stroke="#283473" stroke-width="1"/></svg>mdtrailcraftfair@quorvex.com</li>
      <li><svg class="contact__icon" viewBox="0 0 10 10"><circle cx="5" cy="5" r="4.2" fill="none" stroke="#fff" stroke-width="1.2"/><path d="M0.8 5 H9.2 M5 0.8 C2.5 3.5 2.5 6.5 5 9.2 M5 0.8 C7.5 3.5 7.5 6.5 5 9.2" fill="none" stroke="#fff" stroke-width="1"/></svg>www.mdtrailcraftfair.com</li>
    </ul>
  </div>
  <div class="rule" style="left:195px; top:670px; width:341px"></div>

  <div class="footer-band"></div>
  <div class="venue">
    <span class="venue__pin"><svg width="12" height="16" viewBox="0 0 12 16"><path d="M6 0 C2.7 0 0 2.6 0 5.9 C0 10 6 16 6 16 C6 16 12 10 12 5.9 C12 2.6 9.3 0 6 0 Z" fill="#fff"/><circle cx="6" cy="6" r="2.2" fill="var(--pin)"/></svg></span>
    <span class="venue__text">Pelling Valley Expo, 4837 Orchardmill Rd<br>East Calverton, MD. 21652</span>
  </div>
</section>

</body>
</html>
```